Webdesign für Gebäudereinigung
Zielgruppe
Seit 2005 ist LUM Dienstleistungen der Partner für Gebäudereinigung in Berlin. Wir haben Firmenkunden sowie privat Kunden und kümmern uns um sämtliche Reinigungen. Wie Glasreinigung, Büro- und Unterhaltungsreinigung, Bau- und Baufeinreinigung, Aufgangsreinigung & Grundreinigung…
Aufgabenstellung
Unsere neue Webseite sollte modern - Zeitlos - freundlich sein … Farben am Logo orientieren, das übernehmen wir weiterhin….

```html
<!DOCTYPE html>
<html lang="de">
<head>
<meta charset="utf-8">
<title>LUM Dienstleistungen – Gebäudereinigung in Berlin</title>
<link rel="stylesheet" href="https://fonts.googleapis.com/css2?family=Roboto+Condensed:wght@300;400;500&display=swap">
<style>
:root{
  --navy:#2c4b7c;
  --orange:#f26522;
  --text:#5b6270;
  --muted:#8b93a3;
  --line:#e3e6ec;
  --tint:#dfe4ef;
  --card-blue:#5a7bba;
  --footer:#444;
  --white:#fff;
}
*{box-sizing:border-box;margin:0;padding:0}
html,body{width:1200px;height:2769px;overflow:hidden;background:var(--white)}
body{position:relative;font-family:"Roboto Condensed",sans-serif;color:var(--text)}
.abs{position:absolute}
.btn{position:absolute;display:flex;align-items:center;justify-content:center;background:var(--orange);color:var(--white);font-size:12px;font-weight:500}
/* header */
.logo-mark{left:125px;top:0;width:52px;height:62px;background:var(--navy)}
.logo-name{left:184px;top:48px;font-size:13px;color:var(--navy)}
.top-info{top:7px;font-size:10px;color:var(--navy);display:flex;align-items:center;gap:6px}
.top-phone{left:935px;top:2px;font-size:18px;font-weight:300;color:var(--navy);display:flex;align-items:center;gap:8px}
.nav{top:43px;left:397px;display:flex;gap:26px;font-size:12px;color:#333}
/* hero */
.hero{left:0;top:69px;width:1200px;height:405px;background:linear-gradient(120deg,#c6cfe3 0%,#9aaad0 40%,#8395c3 70%,#6f83b5 100%)}
.hero-kicker{top:184px;width:1200px;text-align:center;color:var(--white);font-size:15px;font-weight:500}
.hero-title{top:208px;width:1200px;text-align:center;color:var(--white);font-size:40px;font-weight:500}
.booking{left:297px;top:281px;width:609px;height:68px;background:var(--navy)}
.field{position:absolute;top:18px;height:32px;background:var(--white);font-size:10px;color:#999;display:flex;align-items:center;padding:0 7px;justify-content:space-between}
/* features */
.feature{width:230px;text-align:center}
.feature h3{font-size:18px;font-weight:400;color:var(--navy);margin-top:14px}
.feature p{font-size:11px;line-height:16px;color:var(--text);margin-top:16px}
.dots{margin-top:14px;display:flex;justify-content:center;gap:4px}
.dots i{width:5px;height:5px;border-radius:50%;background:var(--orange)}
.icon-wrap{position:relative;width:70px;height:70px;margin:0 auto}
.icon-wrap::before{content:"";position:absolute;right:0;bottom:0;width:38px;height:38px;background:var(--tint)}
.icon-wrap svg{position:relative}
/* services */
.section-title{width:1200px;text-align:center;font-size:26px;font-weight:500;color:var(--navy)}
.card{position:absolute;width:225px;height:324px;border:1px solid var(--line);background:var(--white)}
.card .photo{position:absolute;left:0;top:0;width:223px;height:137px}
.card .badge{position:absolute;left:12px;top:106px;width:49px;height:49px;background:var(--white);border:1px solid #c9d1e1;display:flex;align-items:center;justify-content:center}
.card h3{position:absolute;left:12px;top:174px;font-size:18px;font-weight:400;color:var(--navy)}
.card p{position:absolute;left:12px;top:212px;width:200px;font-size:11px;line-height:16px}
.card .btn{left:12px;top:278px;width:68px;height:25px}
.card.special{background:var(--card-blue);border:none;text-align:center;color:var(--white)}
/* how */
.how{left:0;top:1719px;width:1200px;height:431px;background:linear-gradient(100deg,#51679a 0%,#6a80b4 45%,#8092c0 75%,#6d81b2 100%)}
.step-ring{position:absolute;width:146px;height:146px;border-radius:50%;border:1px solid rgba(255,255,255,.85)}
.step{position:absolute;width:108px;height:108px;border-radius:50%;background:var(--white);display:flex;align-items:center;justify-content:center;text-align:center;color:var(--navy);font-size:18px;line-height:21px;font-weight:500}
.num{position:absolute;width:34px;height:34px;border-radius:50%;background:var(--orange);color:var(--white);font-size:17px;display:flex;align-items:center;justify-content:center}
/* about */
.about-title{left:244px;top:2287px;font-size:26px;font-weight:500;color:var(--navy)}
.about-text{left:244px;top:2350px;width:282px;font-size:11px;line-height:20px}
.about-text p+p{margin-top:12px}
.outline-btn{position:absolute;border:1px solid var(--orange);color:var(--orange);font-size:11px;font-weight:500;display:flex;align-items:center;justify-content:center}
.contact-phone{left:548px;top:2265px;font-size:18px;font-weight:300;color:var(--navy);display:flex;align-items:center;gap:8px}
.contact-addr{left:548px;top:2301px;font-size:15px;line-height:25px;color:var(--navy)}
.footer{left:0;top:2707px;width:1200px;height:62px;background:var(--footer);color:var(--white);font-size:8px;display:flex;align-items:center;justify-content:center}
</style>
</head>
<body>

<header>
  <div class="abs logo-mark"></div>
  <div class="abs logo-name">LUM Dienstleistungen</div>
  <div class="abs top-info" style="left:642px">
    <svg width="9" height="11" viewBox="0 0 9 11"><path d="M4.5 0C2 0 0 2 0 4.4 0 7.5 4.5 11 4.5 11S9 7.5 9 4.4C9 2 7 0 4.5 0z" fill="#2c4b7c"/><circle cx="4.5" cy="4.3" r="1.6" fill="#fff"/></svg>
    L.U.M. Dienstleistungen, Lindenhofstr. 14, 10965 Berlin
  </div>
  <div class="abs top-phone">
    <svg width="13" height="13" viewBox="0 0 24 24"><path d="M6.6 10.8a15 15 0 006.6 6.6l2.2-2.2a1 1 0 011-.25 11.4 11.4 0 003.6.57 1 1 0 011 1V20a1 1 0 01-1 1A17 17 0 013 4a1 1 0 011-1h3.5a1 1 0 011 1c0 1.25.2 2.45.57 3.57a1 1 0 01-.25 1z" fill="#2c4b7c"/></svg>
    030 · 482 · 655 · 17
  </div>
  <nav class="abs nav">
    <span>Aufgangsreinigung</span><span>Bauereinigung</span><span>Büroreinigung</span><span>Glasreinigung</span><span>Grundreinigung</span><span>Kontakt</span>
  </nav>
  <div class="btn" style="left:935px;top:35px;width:140px;height:27px">Reinigungstermin buchen</div>
</header>

<section>
  <div class="abs hero" role="img" aria-label="Helle moderne Bürolobby mit Glasfassade, blau getönt"></div>
  <div class="abs hero-kicker">KOMPETENTER PARTNER FÜR DIE OBJEKTREINIGUNG</div>
  <h1 class="abs hero-title">L.U.M. Gebäudereinigung in Berlin</h1>
  <div class="abs booking">
    <div class="field" style="left:37px;width:80px">Quadrat <span style="color:var(--navy)">m²</span></div>
    <div class="field" style="left:124px;width:115px">Date
      <svg width="12" height="12" viewBox="0 0 12 12"><rect x="1" y="2" width="10" height="9" fill="none" stroke="#2c4b7c"/><path d="M1 5h10M3 0v3M9 0v3" stroke="#2c4b7c"/></svg></div>
    <div class="field" style="left:246px;width:176px">Reinigungsart <span style="color:var(--navy);font-size:8px">▼</span></div>
    <div class="btn" style="left:428px;top:18px;width:144px;height:32px">Termin buchen</div>
  </div>
</section>

<section>
  <div class="abs feature" style="left:241px;top:573px">
    <div class="icon-wrap"><svg width="70" height="70" viewBox="0 0 70 70"><circle cx="28" cy="27" r="23" fill="none" stroke="#f26522" stroke-width="2"/><circle cx="28" cy="27" r="18" fill="none" stroke="#f26522"/><path d="M28 15v12l8 5" fill="none" stroke="#f26522" stroke-width="2"/></svg></div>
    <h3>Flexibil &amp; pünktlich</h3>
    <p>Flexibilität bedeutet im Bereich der Gebäude- und Aufgangsreinigung, dass wir problemlos auch kurzfristige Aufträge übernehmen.</p>
    <div class="dots"><i></i><i></i><i></i></div>
  </div>
  <div class="abs feature" style="left:484px;top:573px">
    <div class="icon-wrap"><svg width="70" height="70" viewBox="0 0 70 70" fill="none" stroke="#f26522" stroke-width="1.6"><path d="M28 4l2.5 5 5.5.8-4 3.9 1 5.5-5-2.6-5 2.6 1-5.5-4-3.9 5.5-.8z"/><path d="M12 12l1.8 3.6 4 .6-2.9 2.8.7 4-3.6-1.9-3.6 1.9.7-4-2.9-2.8 4-.6z"/><path d="M44 12l1.8 3.6 4 .6-2.9 2.8.7 4-3.6-1.9-3.6 1.9.7-4-2.9-2.8 4-.6z"/><circle cx="28" cy="34" r="6"/><path d="M16 52c0-7 5-11 12-11s12 4 12 11z"/></svg></div>
    <h3>Kundig &amp; zuverlässig</h3>
    <p>Wir halten Wort, sowohl, was den Umfang unserer Arbeit als auch den Zeitpunkt der Ausführung angeht.</p>
    <div class="dots"><i></i><i></i><i></i></div>
  </div>
  <div class="abs feature" style="left:730px;top:573px">
    <div class="icon-wrap"><svg width="70" height="70" viewBox="0 0 70 70" fill="none" stroke="#f26522" stroke-width="1.8"><path d="M14 30h8v22h-8z"/><path d="M22 32l8-14c3 0 4 2 3 6l-2 6h12c3 0 4 3 2 5 2 2 1 4-1 5 1 2 0 4-2 4 1 3-1 5-3 5H22"/><path d="M42 4l1.5 4 4 1.5-4 1.5L42 15l-1.5-4-4-1.5 4-1.5zM52 16l1 3 3 1-3 1-1 3-1-3-3-1 3-1z"/></svg></div>
    <h3>Gründlich &amp; sauber</h3>
    <p>LUM Dienstleistungen führt die Aufträge einerseits schnell, vor allem aber gewissenhaft und mit penibler Sauberkeit aus.</p>
    <div class="dots"><i></i><i></i><i></i></div>
  </div>
</section>

<section>
  <h2 class="abs section-title" style="top:866px">Leistungen</h2>

  <article class="card" style="left:244px;top:934px">
    <div class="photo" role="img" aria-label="Helles Büro mit bunten Wandbildern" style="background:linear-gradient(90deg,#b7a2a6,#d9dde3 55%,#eef1f4)"></div>
    <div class="badge"><svg width="26" height="28" viewBox="0 0 26 28" fill="none" stroke="#2c4b7c"><rect x="6" y="4" width="14" height="23"/><path d="M9 8h3M14 8h3M9 12h3M14 12h3M9 16h3M14 16h3M11 27v-5h4v5M2 27h22"/></svg></div>
    <h3>Büroreinigung</h3>
    <p>Lorem ipsum dolor sit amet, consectetur adipiscing elit. Sit varius ultricies purus interdum sed. In consequat id ultricies sed</p>
    <div class="btn">Bestellen</div>
  </article>

  <article class="card" style="left:487px;top:934px">
    <div class="photo" role="img" aria-label="Wohnzimmer mit Sofa und grüner Wand" style="background:linear-gradient(90deg,#d9d4cc,#9c7a5f 40%,#6c8a80 60%,#e6e6e2)"></div>
    <div class="badge"><svg width="30" height="26" viewBox="0 0 30 26" fill="none" stroke="#2c4b7c"><rect x="10" y="3" width="14" height="21"/><path d="M13 7h2M17 7h2M21 7h1M13 11h2M17 11h2M13 15h2M17 15h2M1 24h28"/><circle cx="5" cy="16" r="3"/><path d="M5 19v5"/></svg></div>
    <h3>Bauereinigung</h3>
    <p>Lorem ipsum dolor sit amet, consectetur adipiscing elit. Sit varius ultricies purus interdum sed. In consequat id ultricies sed</p>
    <div class="btn">Bestellen</div>
  </article>

  <article class="card" style="left:731px;top:934px">
    <div class="photo" role="img" aria-label="Weiße Küche mit Hängeleuchten und Barhockern" style="background:linear-gradient(180deg,#f1f1f1,#d8d8d8 55%,#4a4a4a)"></div>
    <div class="badge"><svg width="30" height="26" viewBox="0 0 30 26" fill="none" stroke="#2c4b7c"><path d="M3 13L15 3l12 10M6 11v13h18V11"/><rect x="12" y="16" width="6" height="8"/></svg></div>
    <h3>Grundreinigung</h3>
    <p>Lorem ipsum dolor sit amet, consectetur adipiscing elit. Sit varius ultricies purus interdum sed. In consequat id ultricies sed</p>
    <div class="btn">Bestellen</div>
  </article>

  <article class="card" style="left:244px;top:1295px">
    <div class="photo" role="img" aria-label="Glasfassade eines Hochhauses" style="background:linear-gradient(180deg,#8fa3b8,#5e6f82 50%,#a9b9c8)"></div>
    <div class="badge"><svg width="26" height="26" viewBox="0 0 26 26" fill="none" stroke="#2c4b7c"><rect x="2" y="2" width="22" height="22"/><rect x="5" y="5" width="16" height="16"/><path d="M8 18L18 8M12 19l7-7"/></svg></div>
    <h3>Glasreinigung</h3>
    <p>Lorem ipsum dolor sit amet, consectetur adipiscing elit. Sit varius ultricies purus interdum sed. In consequat id ultricies sed</p>
    <div class="btn">Bestellen</div>
  </article>

  <article class="card" style="left:487px;top:1295px">
    <div class="photo" role="img" aria-label="Treppenhaus mit Wendeltreppe" style="background:linear-gradient(90deg,#7d7a4a,#9c9a6a 40%,#3c4a3a 60%,#a3b08a)"></div>
    <div class="badge"><svg width="26" height="28" viewBox="0 0 26 28" fill="none" stroke="#2c4b7c"><rect x="5" y="3" width="16" height="22"/><rect x="8" y="7" width="10" height="7"/><path d="M13 7v7M2 25h22"/></svg></div>
    <h3>Aufgangsreinigung</h3>
    <p>Lorem ipsum dolor sit amet, consectetur adipiscing elit. Sit varius ultricies purus interdum sed. In consequat id ultricies sed</p>
    <div class="btn">Bestellen</div>
  </article>

  <article class="card special" style="left:731px;top:1295px">
    <div class="abs" style="left:0;top:24px;width:225px;font-size:18px">Nicht genormt?</div>
    <div class="abs" style="left:62px;top:68px;width:101px;height:101px;background:var(--white);display:flex;align-items:center;justify-content:center">
      <svg width="52" height="52" viewBox="0 0 52 52" fill="none" stroke="#2c4b7c" stroke-width="1.5"><circle cx="26" cy="20" r="6"/><path d="M14 44V36c0-6 5-9 12-9s12 3 12 9v8z"/><path d="M8 10l2 2M44 10l-2 2M26 4v3M6 24h3M43 24h3" stroke-dasharray="2 2"/></svg>
    </div>
    <p class="abs" style="left:16px;top:193px;width:193px;font-size:11px;line-height:16px">Lorem ipsum dolor sit amet, consectetur adipiscing elit. Sit ultricies purus interdum sed. In consequat id ultricies sed</p>
    <div class="btn" style="left:54px;top:257px;width:116px;height:25px">Individuelle Anfrage</div>
  </article>
</section>

<section>
  <div class="abs how" role="img" aria-label="Großzügige Empfangshalle mit Fensterfront, blau getönt"></div>
  <div class="abs" style="top:1787px;width:1200px;text-align:center;color:var(--white);font-size:11px;font-weight:500">MEHR ERFAHREN</div>
  <h2 class="abs" style="top:1814px;width:1200px;text-align:center;color:var(--white);font-size:26px;font-weight:500">Wie es funktioniert</h2>
  <svg class="abs" style="left:0;top:1719px" width="1200" height="431" viewBox="0 0 1200 431" fill="none" stroke="#fff" stroke-dasharray="4 4">
    <path d="M420 180C460 140 530 140 560 180"/>
    <path d="M640 265C690 300 760 290 790 270"/>
  </svg>
  <div class="step-ring" style="left:281px;top:1871px"></div>
  <div class="step" style="left:300px;top:1890px">Sie<br>buchen</div>
  <div class="num" style="left:371px;top:1890px">1</div>
  <div class="step-ring" style="left:526px;top:1871px"></div>
  <div class="step" style="left:545px;top:1890px">Wir<br>bestätigen</div>
  <div class="num" style="left:616px;top:1890px">2</div>
  <div class="step-ring" style="left:769px;top:1871px"></div>
  <div class="step" style="left:788px;top:1890px">Genießen Sie<br>Sauberkeit</div>
  <div class="num" style="left:860px;top:1890px">3</div>
  <div class="btn" style="left:496px;top:2055px;width:85px;height:26px">Preise prüfen</div>
  <div class="outline-btn" style="left:587px;top:2055px;width:118px;height:26px;border-color:var(--white);color:var(--white);font-size:12px">Kontaktieren Sie uns</div>
</section>

<section>
  <h2 class="abs about-title">Über uns</h2>
  <div class="abs about-text">
    <p>Lorem ipsum dolor sit amet, consectetur adipiscing elit. Facilisi risus, ac eget natoque lectus tincidunt id laoreet. Consectetur dui velit odio tempus nullam non blandit amet. Risus posuere convallis id ligula dui semper amet, mattis.</p>
    <p>Vulputate aliquet at id at eget. Arcu ut nisl nisl sed auctor bibendum. Et diam ut nisi, eget amet, maecenas laoreet. In ac nulla purus tellus nulla sit aenean vitae. Sollicitudin massa purus, elementum, diam.</p>
  </div>
  <div class="outline-btn" style="left:244px;top:2549px;width:117px;height:26px">Kontaktieren Sie uns</div>
  <div class="abs contact-phone">
    <svg width="13" height="13" viewBox="0 0 24 24"><path d="M6.6 10.8a15 15 0 006.6 6.6l2.2-2.2a1 1 0 011-.25 11.4 11.4 0 003.6.57 1 1 0 011 1V20a1 1 0 01-1 1A17 17 0 013 4a1 1 0 011-1h3.5a1 1 0 011 1c0 1.25.2 2.45.57 3.57a1 1 0 01-.25 1z" fill="#2c4b7c"/></svg>
    030 · 482 · 655 · 17
  </div>
  <div class="abs contact-addr">L.U.M. Dienstleistungen,<br>Lindenhofstr. 14,<br>10965 Berlin</div>
  <div class="abs" role="img" aria-label="Sprühflaschen und Reinigungsmittel" style="left:731px;top:2251px;width:225px;height:287px;background:linear-gradient(160deg,#d9d9d9,#f4f4f4 50%,#e8c9c0)"></div>
  <div class="abs" role="img" aria-label="Team sitzt gemeinsam am Wasser bei Sonnenuntergang" style="left:548px;top:2400px;width:286px;height:206px;background:linear-gradient(180deg,#e9e2da,#c9bfb3 50%,#5d6f8e 80%,#8a7a5e);border-right:8px solid #fff;border-top:8px solid #fff"></div>
</section>

<footer class="abs footer">Copyright Gebäudereinigung LUM</footer>

</body>
</html>
```